Software company needs a great powerpoint template

We need a powerpoint template for our growing company. Our software helps hospitals achieve quality via automating tedius manual tasks, performing them better, faster and easier than a person can. See our logo below and check out our website at qrn-medivault.com for more ideas/informaton. We will use this template for sales presentations, trade show demonstrations and partnership proposals.

Target Market(s)

Hospital managers & directors

Industry/Entity Type

Hospital

Contact Information for Business Card

name, title, office telephone, cell phone, email and website

Font styles to use
Sans Serif

Colors
2f74b3
33b8a4

Requirements
Must have
• use blues and greens, san serif fonts
Nice to have
• modern feel yet still somewhat converative

```html
<!DOCTYPE html>
<html lang="en">
<head>
<meta charset="utf-8">
<title>QRN Presentation Template</title>
<link href="https://fonts.googleapis.com/css2?family=Open+Sans:ital,wght@0,400;0,600;0,700;1,400&family=Roboto+Condensed:wght@400;700&display=swap" rel="stylesheet">
<style>
:root{
  --blue:#1f5fae;
  --blue-dark:#17498a;
  --blue-mid:#2f74b3;
  --blue-light:#5d9ad6;
  --green:#3aa83f;
  --teal:#33b8a4;
  --grey-bg:#d4d6d9;
  --grey-line:#8c8c8c;
  --text:#555a60;
  --white:#ffffff;
}
*{margin:0;padding:0;box-sizing:border-box}
html,body{width:1200px;height:902px;overflow:hidden;background:var(--grey-bg)}
body{font-family:"Open Sans",Arial,sans-serif;color:var(--text)}
.stage{position:absolute;left:0;top:0;width:1500px;height:1125px;transform:scale(.8);transform-origin:0 0}
.slide{position:absolute;width:360px;height:202px;background:var(--white);overflow:hidden}
.c1{left:180px}.c2{left:548px}.c3{left:916px}
.r1{top:52px}.r2{top:260px}.r3{top:468px}.r4{top:676px}.r5{top:884px}
.abs{position:absolute}
.title{position:absolute;left:14px;top:15px;font-family:"Roboto Condensed",Arial,sans-serif;font-size:10px;color:var(--blue);text-transform:uppercase;letter-spacing:-.2px;text-decoration:underline;text-decoration-thickness:.5px;text-underline-offset:1px}
.subtitle{position:absolute;left:14px;top:28px;font-family:"Roboto Condensed",Arial,sans-serif;font-size:5px;color:#777;text-transform:uppercase}
.copy{font-size:4.3px;line-height:1.65;color:var(--text);text-align:justify}
.copy b{color:var(--blue);font-weight:600}
.lead{font-size:4.4px;font-weight:600;color:var(--blue);display:block}
.lead.green{color:var(--green)}
.brand{position:absolute;font-family:"Roboto Condensed",Arial,sans-serif;font-weight:700;color:var(--blue);letter-spacing:.5px}
.brand-small{left:6px;bottom:5px;font-size:9px}
.rule{position:absolute;left:0;bottom:2px;width:300px;height:2px;background:var(--grey-line)}
.tab{position:absolute;right:0;bottom:0;width:84px;height:6px;background:var(--blue);clip-path:polygon(8px 0,100% 0,100% 100%,0 100%)}
.pageno{position:absolute;right:6px;bottom:1px;font-size:3.5px;color:var(--white)}
.photo{position:absolute}
.img-lab{background:linear-gradient(135deg,#dfe8f1,#9fb8d3 55%,#c74a56 90%)}
.img-tech{background:linear-gradient(135deg,#3c6fa8,#a9c6e4 50%,#2c5e97)}
.img-people{background:linear-gradient(90deg,#f3f4f6,#4a4f58 30%,#e6e8ec 50%,#3b3f46 75%,#eef0f3)}
.img-room{background:linear-gradient(135deg,#f0f3f6,#c7d2dc 60%,#9aabbd)}
.cell{position:absolute;width:90px;height:68px;padding:22px 7px 0;font-size:4.2px;font-weight:700;line-height:1.5;color:var(--white);text-transform:uppercase}
.cell.blue{background:var(--blue)}
.cell.green{background:var(--green)}
.toc{position:absolute;display:flex;align-items:center;gap:6px}
.toc-num{width:11px;height:11px;border-radius:50%;background:var(--green);color:var(--white);font-size:5px;display:flex;align-items:center;justify-content:center;border:1px solid #9fd6a1}
.toc-text{font-size:4.3px;font-weight:700;line-height:1.45;color:var(--white);text-transform:uppercase}
.service{position:absolute;width:66px;text-align:center}
.service .icon{width:28px;height:28px;border-radius:50%;background:var(--blue);margin:0 auto 8px;display:flex;align-items:center;justify-content:center}
.service .name{font-size:4.2px;font-weight:700;color:var(--blue);text-transform:uppercase}
.service .copy,.member .copy,.donut-col .copy{text-align:center;line-height:1.45}
.member{position:absolute;width:86px;text-align:center}
.avatar{width:42px;height:42px;border-radius:50%;margin:0 auto 5px;border:2px solid var(--blue);background:radial-gradient(circle at 50% 40%,#e6e8eb,#7d838b 70%,#2f3338)}
.member .name{font-size:4.5px;font-weight:700;color:var(--green);text-transform:uppercase}
.member .role{font-size:3.8px;font-style:italic;color:#666;margin-bottom:10px}
.donut-col{position:absolute;width:80px;text-align:center}
.donut-col svg{display:block;margin:0 auto 8px}
.bullet{position:absolute;left:68px;width:280px}
.bullet .lead::before{content:"\203A";margin-right:3px;color:var(--blue)}
.legend{position:absolute;font-size:3.6px;line-height:1.4;color:var(--text)}
.legend .key{display:inline-block;width:4px;height:4px;margin-right:3px;vertical-align:middle}
.contact{position:absolute;left:28px;display:flex;align-items:center;gap:6px;font-size:5px;color:var(--white)}
.contact svg{flex:none}
</style>
</head>
<body>
<div class="stage">

<!-- Cover -->
<section class="slide c1 r1">
  <div class="brand" style="left:26px;top:38px;font-size:28px">QRN</div>
  <div class="abs" style="left:0;top:80px;width:360px;height:80px;background:var(--blue)"></div>
  <div class="photo img-tech" role="img" aria-label="Hand touching a glowing hexagon interface" style="left:0;top:80px;width:200px;height:80px;-webkit-mask-image:linear-gradient(90deg,#000 60%,transparent);mask-image:linear-gradient(90deg,#000 60%,transparent)"></div>
  <div class="abs" style="left:0;top:160px;width:360px;height:2px;background:var(--green)"></div>
  <div class="abs" style="right:20px;top:86px;text-align:right;color:var(--white)">
    <div style="font-family:'Roboto Condensed',sans-serif;font-size:16px;letter-spacing:.3px">WELCOME</div>
    <div style="font-family:'Roboto Condensed',sans-serif;font-size:9px;letter-spacing:2px">TO OUR PRESENTATION</div>
    <div style="font-size:5px;font-weight:600;margin-top:5px">Birmingham, March 25, 2016</div>
  </div>
  <div class="abs copy" style="left:32px;top:176px;width:180px;font-size:3px;line-height:1.4">© 2017 All rights reserved. Contains confidential and proprietary information and may not be disclosed or reproduced without the prior written consent of QRN.</div>
  <div class="abs" style="left:0;bottom:0;width:360px;height:3px;background:var(--blue)"></div>
</section>

<!-- Table of contents -->
<section class="slide c2 r1" style="background:var(--blue)">
  <div class="photo" role="img" aria-label="Blurred medical technology icons over a blue screen" style="inset:0;background:radial-gradient(circle at 45% 25%,#4e8fd0,#1f5fae 55%,#174a8c)"></div>
  <div class="abs" style="left:38px;top:52px;color:var(--white);font-family:'Roboto Condensed',sans-serif">
    <div style="font-size:5px">TABLE OF</div>
    <div style="font-size:13px;margin-top:-1px">CONTENTS</div>
  </div>
  <div class="toc" style="left:60px;top:104px"><span class="toc-num">1</span><span class="toc-text">Lorem ipsum dolor sit<br>met dolor sit met</span></div>
  <div class="toc" style="left:60px;top:132px"><span class="toc-num">1</span><span class="toc-text">Lorem ipsum dolor sit<br>met dolor sit met</span></div>
  <div class="toc" style="left:60px;top:158px"><span class="toc-num">1</span><span class="toc-text">Lorem ipsum dolor sit<br>met dolor sit met</span></div>
  <div class="toc" style="left:188px;top:104px"><span class="toc-num">1</span><span class="toc-text">Lorem ipsum dolor sit<br>met dolor sit met</span></div>
  <div class="toc" style="left:188px;top:132px"><span class="toc-num">1</span><span class="toc-text">Lorem ipsum dolor sit<br>met dolor sit met</span></div>
  <div class="toc" style="left:188px;top:158px"><span class="toc-num">1</span><span class="toc-text">Lorem ipsum dolor sit<br>met dolor sit met</span></div>
</section>

<!-- About us: team band -->
<section class="slide c3 r1">
  <div class="title">About Us</div><div class="subtitle">Subtitle goes here</div>
  <div class="abs" style="left:0;top:52px;width:118px;height:66px;background:var(--blue)"></div>
  <div class="abs toc-text" style="left:14px;top:74px;width:96px;font-size:4px">Lorem ipsum dolor sit met consectetur adipiscing elit, sed do eiusmod tempor incididunt ut labore et dolore magna</div>
  <div class="photo img-people" role="img" aria-label="Group of business professionals in suits" style="left:118px;top:52px;width:242px;height:66px"></div>
  <div class="abs" style="left:0;top:118px;width:360px;height:1px;background:var(--blue)"></div>
  <p class="abs copy" style="left:118px;top:128px;width:230px">Lorem ipsum dolor sit amet, consectetur adipiscing elit, sed do eiusmod tempor incididunt ut labore et dolore magna aliqua. Ut enim ad minim veniam, quis nostrud exercitation ullamco laboris nisi ut aliquip ex ea commodo consequat. Duis aute irure dolor in reprehenderit in voluptate velit esse cillum dolore eu fugiat nulla pariatur.</p>
  <p class="abs copy" style="left:118px;top:168px;width:230px">Lorem ipsum dolor sit amet, consectetur adipiscing elit, sed do eiusmod tempor incididunt ut labore et dolore magna aliqua. Ut enim ad minim veniam, quis nostrud exercitation ullamco laboris nisi ut aliquip ex ea commodo consequat.</p>
  <div class="brand brand-small">QRN</div><div class="rule"></div><div class="tab"></div><span class="pageno">02</span>
</section>

<!-- About us: two columns -->
<section class="slide c1 r2">
  <div class="title">About Us</div><div class="subtitle">Subtitle goes here</div>
  <div class="photo img-tech" role="img" aria-label="Hand tapping medical icons on a touch screen" style="left:19px;top:60px;width:74px;height:48px"></div>
  <div class="abs lead green" style="left:19px;top:114px;width:76px;text-align:right;line-height:1.5">Lorem ipsum dolor sit amet consectetur adipiscing elitsed do eiusmod</div>
  <p class="abs copy" style="left:108px;top:60px;width:112px"><span class="lead">Lorem ipsum dolor sit amet</span>consectetur adipiscing elit, sed do eiusmod tempor incididunt ut labore et dolore magna aliqua. Ut enim ad minim veniam, quis nostrud exercitation ullamco laboris nisi ut aliquip ex ea commodo consequat. Duis aute irure dolor in reprehenderit in voluptate velit esse cillum dolore eu fugiat nulla pariatur.</p>
  <p class="abs copy" style="left:228px;top:60px;width:112px"><span class="lead">Lorem ipsum dolor sit amet</span>consectetur adipiscing elit, sed do eiusmod tempor incididunt ut labore et dolore magna aliqua. Ut enim ad minim veniam, quis nostrud exercitation ullamco laboris nisi ut aliquip ex ea commodo consequat. Duis aute irure dolor in reprehenderit in voluptate velit esse cillum dolore eu fugiat nulla pariatur.</p>
  <p class="abs copy" style="left:108px;top:132px;width:112px"><span class="lead">Lorem ipsum dolor sit amet</span>consectetur adipiscing elit, sed do eiusmod tempor incididunt ut labore et dolore magna aliqua. Ut enim ad minim veniam, quis nostrud exercitation ullamco laboris nisi ut aliquip ex ea</p>
  <p class="abs copy" style="left:228px;top:132px;width:112px"><span class="lead">Lorem ipsum dolor sit amet</span>consectetur adipiscing elit, sed do eiusmod tempor incididunt ut labore et dolore magna aliqua. Ut enim ad minim veniam, quis nostrud exercitation ullamco laboris nisi ut aliquip ex ea</p>
  <div class="brand brand-small">QRN</div><div class="rule"></div><div class="tab"></div><span class="pageno">02</span>
</section>

<!-- About us: grid -->
<section class="slide c2 r2">
  <div class="title">About Us</div><div class="subtitle">Subtitle goes here</div>
  <div class="photo img-lab" role="img" aria-label="Laboratory sample tubes" style="left:0;top:44px;width:90px;height:68px"></div>
  <div class="cell blue" style="left:90px;top:44px">Lorem ipsum dolor sit met consectetur adipiscing elit, sed do eiusmod tempor inc ididunt ut labore et</div>
  <div class="photo img-tech" role="img" aria-label="Digital medical interface" style="left:180px;top:44px;width:90px;height:68px"></div>
  <div class="cell blue" style="left:270px;top:44px">Lorem ipsum dolor sit met consectetur adipiscing elit, sed do eiusmod tempor inc ididunt ut labore et</div>
  <div class="cell green" style="left:0;top:112px">Lorem ipsum dolor sit met consectetur adipiscing elit, sed do eiusmod tempor inc ididunt ut labore et</div>
  <div class="photo img-room" role="img" aria-label="Hospital laboratory room" style="left:90px;top:112px;width:90px;height:68px"></div>
  <div class="cell green" style="left:180px;top:112px">Lorem ipsum dolor sit met consectetur adipiscing elit, sed do eiusmod tempor inc ididunt ut labore et</div>
  <div class="photo img-tech" role="img" aria-label="Hand touching health icons" style="left:270px;top:112px;width:90px;height:68px"></div>
  <div class="brand brand-small">QRN</div><div class="rule"></div><div class="tab"></div><span class="pageno">02</span>
</section>

<!-- About us: three images -->
<section class="slide c3 r2">
  <div class="title">About Us</div><div class="subtitle">Subtitle goes here</div>
  <div class="photo img-room" role="img" aria-label="Laboratory equipment" style="left:42px;top:56px;width:86px;height:58px"></div>
  <div class="photo img-tech" role="img" aria-label="Digital medical interface" style="left:137px;top:56px;width:86px;height:58px"></div>
  <div class="photo img-lab" role="img" aria-label="Sample tubes in a rack" style="left:231px;top:56px;width:86px;height:58px"></div>
  <p class="abs copy" style="left:42px;top:120px;width:86px;text-align:left"><span class="lead green">Lorem ipsum dolor sit amet</span><br>Ut enim ad minim veniam, quis nostrud exercitation ullamco laboris nisi ut aliquip ex ea commodo consequat. Duis aute irure dolor in reprehenderit in voluptate velit esse cillum dolore eu fugiat nulla pariatur.</p>
  <p class="abs copy" style="left:137px;top:120px;width:86px;text-align:left"><span class="lead green">Lorem ipsum dolor sit amet</span><br>Ut enim ad minim veniam, quis nostrud exercitation ullamco laboris nisi ut aliquip ex ea commodo consequat. Duis aute irure dolor in reprehenderit in voluptate velit esse cillum dolore eu fugiat nulla pariatur.</p>
  <p class="abs copy" style="left:231px;top:120px;width:86px;text-align:left"><span class="lead green">Lorem ipsum dolor sit amet</span><br>Ut enim ad minim veniam, quis nostrud exercitation ullamco laboris nisi ut aliquip ex ea commodo consequat. Duis aute irure dolor in reprehenderit in voluptate velit esse cillum dolore eu fugiat nulla pariatur.</p>
  <div class="brand brand-small">QRN</div><div class="rule"></div><div class="tab"></div><span class="pageno">02</span>
</section>

<!-- Services -->
<section class="slide c1 r3">
  <div class="title">Our Services</div><div class="subtitle">Subtitle goes here</div>
  <div class="service" style="left:18px;top:66px">
    <div class="icon"><svg width="14" height="14" viewBox="0 0 14 14"><path d="M2 10a5 5 0 0 1 10 0z" fill="#fff"/><path d="M7 10 9.5 6" stroke="#1f5fae" stroke-width="1.2"/></svg></div>
    <div class="name">Lorem ipsum dolor</div>
    <p class="copy">dolor sit amet, consectetur adipiscing elit, sed do eiusmod tempor incididunt ut labore et dolore magna aliqua. Ut enim ad minim veniam, quis nostrud exercitation ullamco laboris nisi ut aliquip ex ea esse cillum</p>
  </div>
  <div class="service" style="left:105px;top:66px">
    <div class="icon"><svg width="14" height="14" viewBox="0 0 14 14" fill="#fff"><rect x="3" y="2" width="2" height="10"/><rect x="7" y="3" width="4" height="1.5"/><rect x="7" y="6" width="4" height="1.5"/><rect x="7" y="9" width="4" height="1.5"/></svg></div>
    <div class="name">Lorem ipsum dolor</div>
    <p class="copy">dolor sit amet, consectetur adipiscing elit, sed do eiusmod tempor incididunt ut labore et dolore magna aliqua. Ut enim ad minim veniam, quis nostrud exercitation ullamco laboris nisi ut aliquip ex ea esse cillum</p>
  </div>
  <div class="service" style="left:195px;top:66px">
    <div class="icon"><svg width="14" height="14" viewBox="0 0 14 14"><text x="7" y="11.5" text-anchor="middle" font-family="Open Sans,sans-serif" font-weight="700" font-size="12" fill="#fff">$</text></svg></div>
    <div class="name">Lorem ipsum dolor</div>
    <p class="copy">dolor sit amet, consectetur adipiscing elit, sed do eiusmod tempor incididunt ut labore et dolore magna aliqua. Ut enim ad minim veniam, quis nostrud exercitation ullamco laboris nisi ut aliquip ex ea esse cillum</p>
  </div>
  <div class="service" style="left:279px;top:66px">
    <div class="icon"><svg width="14" height="14" viewBox="0 0 14 14" fill="#fff"><rect x="2" y="6" width="2.5" height="6"/><path d="M5.5 6 8 2c1.2 0 1.5.8 1.2 2L8.8 6H12c.6 0 1 .5.9 1l-1 4.5c-.1.4-.5.5-.9.5H5.5z"/></svg></div>
    <div class="name">Lorem ipsum dolor</div>
    <p class="copy">dolor sit amet, consectetur adipiscing elit, sed do eiusmod tempor incididunt ut labore et dolore magna aliqua. Ut enim ad minim veniam, quis nostrud exercitation ullamco laboris nisi ut aliquip ex ea esse cillum</p>
  </div>
  <div class="brand brand-small">QRN</div><div class="rule"></div><div class="tab"></div><span class="pageno">02</span>
</section>

<!-- Right image -->
<section class="slide c2 r3">
  <div class="title">Right Image</div><div class="subtitle">Subtitle goes here</div>
  <p class="abs copy" style="left:28px;top:62px;width:164px"><span class="lead">Lorem ipsum dolor sit amet</span>consectetur adipiscing elit, sed do eiusmod tempor incididunt ut labore et dolore magna aliqua. Ut enim ad minim veniam, quis nostrud exercitation ullamco laboris nisi ut aliquip ex ea commodo consequat. Duis aute irure dolor in reprehenderit in voluptate velit esse cillum dolore eu fugiat nulla pariatur.</p>
  <p class="abs copy" style="left:28px;top:118px;width:164px"><span class="lead">Lorem ipsum dolor sit amet</span>consectetur adipiscing elit, sed do eiusmod tempor incididunt ut labore et dolore magna aliqua. Ut enim ad minim veniam, quis nostrud exercitation ullamco laboris nisi ut aliquip ex ea commodo consequat. Duis aute irure dolor in reprehenderit in voluptate velit esse cillum dolore eu</p>
  <div class="photo" role="img" aria-label="Doctor with a clipboard beside a digital health screen" style="left:208px;top:66px;width:136px;height:94px;background:linear-gradient(90deg,#1f74b8,#4fa4da 55%,#e9eef3)"></div>
  <div class="brand brand-small">QRN</div><div class="rule"></div><div class="tab"></div><span class="pageno">02</span>
</section>

<!-- Bullet text -->
<section class="slide c3 r3">
  <div class="title">Bullet Text</div><div class="subtitle">Subtitle goes here</div>
  <p class="bullet copy" style="top:58px"><span class="lead">Lorem ipsum dolor sit amet</span>consectetur adipiscing elit, sed do eiusmod tempor incididunt ut labore et dolore magna aliqua. Ut enim ad minim veniam, quis nostrud exercitation ullamco laboris nisi ut aliquip ex ea commodo consequat. Duis aute irure dolor in reprehenderit in voluptate velit esse cillum dolore eu fugiat nulla pariatur.</p>
  <p class="bullet copy" style="top:95px"><span class="lead">Lorem ipsum dolor sit amet</span>consectetur adipiscing elit, sed do eiusmod tempor incididunt ut labore et dolore magna aliqua. Ut enim ad minim veniam, quis nostrud exercitation ullamco laboris nisi ut aliquip ex ea commodo consequat. Duis aute irure dolor in reprehenderit in voluptate velit esse cillum dolore eu</p>
  <p class="bullet copy" style="top:131px"><span class="lead">Lorem ipsum dolor sit amet</span>Excepteur sint occaecat cupidatat non proident, sunt in culpa qui officia deserunt mollit anim id est laborum. Excepteur sint occaecat cupidatat non proident, sunt in conseqat. Duis aute irure dolor in reprehenderit in voluptate velit esse cillum dolore eu</p>
  <div class="brand brand-small">QRN</div><div class="rule"></div><div class="tab"></div><span class="pageno">02</span>
</section>

<!-- Team -->
<section class="slide c1 r4">
  <div class="title">Our Team</div><div class="subtitle">Subtitle goes here</div>
  <div class="member" style="left:16px;top:62px">
    <div class="avatar" role="img" aria-label="Portrait of a team member"></div>
    <div class="name">Jonathan Doe</div><div class="role">President</div>
    <p class="copy">dolor sit amet, consectetur adipiscing elit, sed do eiusmod tempor incididunt ut labore et dolore magna aliqua. Ut enim ad minim veniam, quis nostrud exercitation ullamco laboris nisi ut aliquip ex ea esse cillum dolore eu fugiat nulla pariatur.</p>
  </div>
  <div class="member" style="left:138px;top:62px">
    <div class="avatar" role="img" aria-label="Portrait of a team member"></div>
    <div class="name">Jonathan Doe</div><div class="role">President</div>
    <p class="copy">dolor sit amet, consectetur adipiscing elit, sed do eiusmod tempor incididunt ut labore et dolore magna aliqua. Ut enim ad minim veniam, quis nostrud exercitation ullamco laboris nisi ut aliquip ex ea esse cillum dolore eu fugiat nulla pariatur.</p>
  </div>
  <div class="member" style="left:260px;top:62px">
    <div class="avatar" role="img" aria-label="Portrait of a team member"></div>
    <div class="name">Jonathan Doe</div><div class="role">President</div>
    <p class="copy">dolor sit amet, consectetur adipiscing elit, sed do eiusmod tempor incididunt ut labore et dolore magna aliqua. Ut enim ad minim veniam, quis nostrud exercitation ullamco laboris nisi ut aliquip ex ea esse cillum dolore eu fugiat nulla pariatur.</p>
  </div>
  <div class="brand brand-small">QRN</div><div class="rule"></div><div class="tab"></div><span class="pageno">02</span>
</section>

<!-- Donut chart -->
<section class="slide c2 r4">
  <div class="title">Our Chart</div><div class="subtitle">Subtitle goes here</div>
  <div class="donut-col" style="left:29px;top:70px">
    <svg width="48" height="48" viewBox="0 0 48 48"><circle cx="24" cy="24" r="20" fill="none" stroke="#b9bcbf" stroke-width="4"/><circle cx="24" cy="24" r="20" fill="none" stroke="var(--blue)" stroke-width="4" stroke-dasharray="101.8 125.7" transform="rotate(-90 24 24)"/><text x="24" y="27" text-anchor="middle" font-family="Roboto Condensed,sans-serif" font-weight="700" font-size="9" fill="var(--blue)">81%</text></svg>
    <p class="copy">dolor sit amet, consectetur adipiscing elit, sed do eiusmod tempor incididunt ut labore et dolore magna aliqua. Ut enim ad minim veniam, quis nostrud exercitation ullamco laboris nisi ut aliquip ex ea esse cillum dolore eu fugiat nulla pariatur.</p>
  </div>
  <div class="donut-col" style="left:135px;top:70px">
    <svg width="48" height="48" viewBox="0 0 48 48"><circle cx="24" cy="24" r="20" fill="none" stroke="#b9bcbf" stroke-width="4"/><circle cx="24" cy="24" r="20" fill="none" stroke="var(--blue)" stroke-width="4" stroke-dasharray="90.5 125.7" transform="rotate(-90 24 24)"/><text x="24" y="27" text-anchor="middle" font-family="Roboto Condensed,sans-serif" font-weight="700" font-size="9" fill="var(--blue)">72%</text></svg>
    <p class="copy">dolor sit amet, consectetur adipiscing elit, sed do eiusmod tempor incididunt ut labore et dolore magna aliqua. Ut enim ad minim veniam, quis nostrud exercitation ullamco laboris nisi ut aliquip ex ea esse cillum dolore eu fugiat nulla pariatur.</p>
  </div>
  <div class="donut-col" style="left:237px;top:70px">
    <svg width="48" height="48" viewBox="0 0 48 48"><circle cx="24" cy="24" r="20" fill="none" stroke="#b9bcbf" stroke-width="4"/><circle cx="24" cy="24" r="20" fill="none" stroke="var(--blue)" stroke-width="4" stroke-dasharray="79.2 125.7" transform="rotate(-90 24 24)"/><circle cx="24" cy="24" r="20" fill="none" stroke="var(--green)" stroke-width="4" stroke-dasharray="12 125.7" stroke-dashoffset="-67" transform="rotate(-90 24 24)"/><text x="24" y="27" text-anchor="middle" font-family="Roboto Condensed,sans-serif" font-weight="700" font-size="9" fill="var(--blue)">63%</text></svg>
    <p class="copy">dolor sit amet, consectetur adipiscing elit, sed do eiusmod tempor incididunt ut labore et dolore magna aliqua. Ut enim ad minim veniam, quis nostrud exercitation ullamco laboris nisi ut aliquip ex ea esse cillum dolore eu fugiat nulla pariatur.</p>
  </div>
  <div class="brand brand-small">QRN</div><div class="rule"></div><div class="tab"></div><span class="pageno">02</span>
</section>

<!-- Bar chart -->
<section class="slide c3 r4">
  <div class="title">Our Chart</div><div class="subtitle">Subtitle goes here</div>
  <p class="abs copy" style="left:44px;top:68px;width:164px"><span class="lead">Lorem ipsum dolor sit amet</span>consectetur adipiscing elit, sed do eiusmod tempor incididunt ut labore et dolore magna aliqua. Ut enim ad minim veniam, quis nostrud exercitation ullamco laboris nisi ut aliquip ex ea commodo consequat. Duis aute irure dolor in reprehenderit in voluptate velit esse cillum dolore eu fugiat nulla pariatur.</p>
  <p class="abs copy" style="left:44px;top:124px;width:164px"><span class="lead">Lorem ipsum dolor sit amet</span>consectetur adipiscing elit, sed do eiusmod tempor incididunt ut labore et dolore magna aliqua. Ut enim ad minim veniam, quis nostrud exercitation ullamco laboris nisi ut aliquip ex ea commodo consequat. Duis aute irure dolor in reprehenderit in voluptate velit esse cillum dolore eu</p>
  <svg class="abs" style="left:240px;top:44px" width="110" height="76" viewBox="0 0 110 76">
    <line x1="6" y1="4" x2="6" y2="66" stroke="#999" stroke-width=".5"/>
    <line x1="6" y1="66" x2="108" y2="66" stroke="#999" stroke-width=".5"/>
    <g fill="var(--blue)"><rect x="10" y="20" width="5" height="46"/><rect x="34" y="32" width="5" height="34"/><rect x="58" y="18" width="5" height="48"/><rect x="82" y="24" width="5" height="42"/></g>
    <g fill="#c4c7ca"><rect x="16" y="40" width="5" height="26"/><rect x="40" y="48" width="5" height="18"/><rect x="64" y="28" width="5" height="38"/><rect x="88" y="38" width="5" height="28"/></g>
    <g fill="var(--green)"><rect x="22" y="44" width="5" height="22"/><rect x="46" y="36" width="5" height="30"/><rect x="70" y="26" width="5" height="40"/><rect x="94" y="20" width="5" height="46"/></g>
    <rect x="56" y="14" width="8" height="3" fill="var(--blue)"/>
    <g font-family="Open Sans,sans-serif" font-size="3.5" fill="#666" text-anchor="middle"><text x="18" y="72">2009</text><text x="42" y="72">2010</text><text x="66" y="72">2011</text><text x="90" y="72">2012</text></g>
  </svg>
  <div class="legend" style="left:262px;top:124px;width:62px"><span class="key" style="background:var(--blue)"></span><b>LOREM IPSUM</b><br>Lorem ipsum dolor sit amet consectetur adipiscing elit sed do eiusmod</div>
  <div class="legend" style="left:262px;top:150px;width:62px"><span class="key" style="background:var(--green)"></span><b>LOREM IPSUM</b><br>Lorem ipsum dolor sit amet consectetur adipiscing elit sed do eiusmod</div>
  <div class="brand brand-small">QRN</div><div class="rule"></div><div class="tab"></div><span class="pageno">02</span>
</section>

<!-- Section title -->
<section class="slide c1 r5" style="background:var(--blue)">
  <div class="photo" role="img" aria-label="Padlock over a field of digital code" style="inset:0;background:radial-gradient(circle at 40% 45%,#3f7fc4,#1f5fae 55%,#174a8c)"></div>
  <svg class="abs" style="left:158px;top:78px" width="44" height="44" viewBox="0 0 44 44"><circle cx="22" cy="22" r="21" fill="#fff"/><circle cx="23" cy="12" r="2.6" fill="var(--green)"/><path d="M19 18h6l-3 14h3v2h-8v-2h2z" fill="var(--green)"/></svg>
  <div class="abs" style="left:0;width:360px;top:138px;text-align:center;color:var(--white);font-family:'Roboto Condensed',sans-serif;font-size:12px">SECTION TITLE</div>
  <div class="abs" style="left:120px;top:156px;width:120px;height:.8px;background:#9dbde0"></div>
</section>

<!-- Image text -->
<section class="slide c2 r5">
  <div class="abs" style="left:0;top:0;width:176px;height:202px;background:var(--blue)"></div>
  <div class="abs" style="left:14px;top:14px;color:var(--white);font-family:'Roboto Condensed',sans-serif">
    <div style="font-size:10px">IMAGE TEXT</div>
    <div style="font-size:5px;margin-top:1px">SUBTITLE GOES HERE</div>
  </div>
  <p class="abs copy" style="left:20px;top:70px;width:134px;color:var(--white);font-weight:600">Lorem ipsum dolor sit amet, consectetur adipiscing elit, sed do eiusmod tempor incididunt ut labore et dolore magna aliqua. Ut enim ad minim veniam, quis nostrud exercitation ullamco laboris nisi ut aliquip ex ea commodo consequat. Duis aute irure dolor in reprehenderit in voluptate velit esse cillum dolore eu fugiat nulla pariatur.</p>
  <p class="abs copy" style="left:20px;top:132px;width:134px;color:var(--white);font-weight:600">Lorem ipsum dolor sit amet, consectetur adipiscing elit, sed do eiusmod tempor incididunt ut labore et dolore</p>
  <div class="photo" role="img" aria-label="Smiling man and woman, black and white portrait" style="left:176px;top:0;width:184px;height:202px;background:linear-gradient(120deg,#f4f4f4,#bdbdbd 45%,#4a4a4a 80%,#d9d9d9)"></div>
  <div class="brand brand-small" style="color:var(--white)">QRN</div>
</section>

<!-- Thank you -->
<section class="slide c3 r5">
  <div class="brand" style="left:24px;top:38px;font-size:26px">QRN</div>
  <div class="abs" style="left:0;top:64px;width:360px;height:136px;background:var(--blue)"></div>
  <div class="photo" role="img" aria-label="Close-up of an eye behind binary code" style="left:150px;top:64px;width:210px;height:136px;background:linear-gradient(90deg,var(--blue),#3f7fc4 60%,#2a68ad)"></div>
  <div class="abs" style="left:28px;top:104px;color:var(--white);font-family:'Roboto Condensed',sans-serif">
    <div style="font-size:9px;font-weight:700">THANK YOU</div>
    <div style="font-size:11px;margin-top:-1px">FOR YOUR TIME</div>
  </div>
  <div class="contact" style="top:146px"><svg width="8" height="8" viewBox="0 0 8 8"><circle cx="4" cy="4" r="3.6" fill="none" stroke="#fff" stroke-width=".7"/><path d="M4 1.8a1.4 1.4 0 0 1 1.4 1.4C5.4 4.3 4 6 4 6S2.6 4.3 2.6 3.2A1.4 1.4 0 0 1 4 1.8z" fill="#fff"/></svg>1420 Harbor Lane Ste 300</div>
  <div class="contact" style="top:163px"><svg width="8" height="8" viewBox="0 0 8 8"><circle cx="4" cy="4" r="3.6" fill="none" stroke="#fff" stroke-width=".7"/><rect x="2.2" y="2.8" width="3.6" height="2.6" fill="#fff"/><path d="M2.2 2.8 4 4.3l1.8-1.5" stroke="var(--blue)" stroke-width=".4" fill="none"/></svg>support@qrn-medivault.com</div>
  <div class="contact" style="top:180px"><svg width="8" height="8" viewBox="0 0 8 8" fill="none" stroke="#fff" stroke-width=".6"><circle cx="4" cy="4" r="3.6"/><circle cx="4" cy="4" r="2"/><path d="M2 4h4M4 2v4"/></svg>www.qrn-medivault.com</div>
  <div class="abs" style="left:0;bottom:0;width:360px;height:3px;background:var(--green)"></div>
</section>

</div>
</body>
</html>
```